Bookmark Design

We would like to design a book mark with logos of our two business and a quote.

One side with the quote "The first wealth is health" - Tobias Quill Harrow and the two logos.

The back side has the two logos with its respective phone numbers and a common address (this is to be advised to the winner of the project).

```html
<!DOCTYPE html>
<html lang="en">
<head>
<meta charset="utf-8">
<title>Bookmark – Brightwater Clinic &amp; Harbour Dental</title>
<link rel="stylesheet" href="https://fonts.googleapis.com/css2?family=Montserrat:wght@600;700;800&family=Roboto+Slab:wght@300;800&family=Oswald:wght@500&display=swap">
<style>
  :root{
    --blue:#0a52a1;
    --green:#7ac142;
    --paper:#f3f4f5;
    --white:#ffffff;
    --stage:#d6d6d6;
  }
  *{margin:0;padding:0;box-sizing:border-box}
  html,body{width:867px;height:1200px;overflow:hidden;background:var(--stage)}
  .canvas{position:relative;width:867px;height:1200px}
  .bookmark{
    position:absolute;top:120px;width:300px;height:1200px;
    transform:scale(.8);transform-origin:top left;
    background:var(--paper);overflow:hidden;
    font-family:"Montserrat",sans-serif;
  }
  .bookmark--front{left:149px}
  .bookmark--back{left:473px}
  .bookmark__bands{position:absolute;inset:0}

  .clinic-brand{position:absolute;left:0;width:300px;top:100px;text-align:center;color:var(--blue)}
  .clinic-brand__mark{width:120px;height:120px;margin:0 auto 22px;border:5px solid var(--blue);border-radius:50%}
  .clinic-brand__name{font-weight:800;font-size:28px;line-height:1;letter-spacing:-.5px}
  .clinic-brand__sub{font-weight:800;font-size:15px;letter-spacing:5px;margin-top:4px}

  .dental-brand{position:absolute;left:0;width:300px;text-align:center;color:var(--green);font-weight:800;line-height:1.02}
  .dental-brand__line{display:block;font-size:34px}
  .dental-brand__line--small{font-size:22px;margin-top:6px}

  /* front quote: positions are in bookmark coordinates */
  .quote{position:absolute;left:0;top:0;width:300px;height:1200px;color:var(--white)}
  .quote__mark{position:absolute;font-family:"Roboto Slab",serif;font-weight:800;font-size:88px;line-height:1}
  .quote__mark--open{left:36px;top:440px}
  .quote__mark--close{left:200px;top:812px}
  .quote__frame{position:absolute;left:110px;top:483px;width:148px;height:247px;border-top:2px solid var(--white);border-right:2px solid var(--white)}
  .quote__text{position:absolute;left:39px;top:525px;font-family:"Roboto Slab",serif;font-size:44px;line-height:54px;white-space:nowrap}
  .quote__text b{font-weight:800}
  .quote__text span{font-weight:300}
  .quote__author{position:absolute;right:108px;top:829px;font-family:"Oswald",sans-serif;font-style:normal;font-weight:500;font-size:11px;letter-spacing:-.2px;white-space:nowrap}

  /* back contact */
  .icon-row{position:absolute;left:30px;width:240px;height:40px;display:flex;align-items:center;justify-content:space-between}
  .icon-row::before,.icon-row::after{content:"";width:85px;height:2px;background:var(--blue)}
  .icon-row--light::before,.icon-row--light::after{background:var(--white)}
  .icon-badge{width:40px;height:40px;border-radius:50%;display:flex;align-items:center;justify-content:center}
  .icon-badge--phone{background:var(--white);border:4px solid var(--green)}
  .icon-badge--pin{background:var(--white)}
  .phone-box{position:absolute;left:30px;width:240px;height:52px;border-radius:4px;background:var(--blue);color:var(--white);font-weight:700;font-size:30px;letter-spacing:.5px;display:flex;align-items:center;justify-content:center}
  .address{position:absolute;left:0;width:300px;top:617px;text-align:center;color:var(--white);font-weight:700;font-size:18px;line-height:26px;font-style:normal}
  .address-rule{position:absolute;left:56px;top:734px;width:188px;height:2px;background:var(--white)}
</style>
</head>
<body>
<main class="canvas">

  <!-- Front -->
  <section class="bookmark bookmark--front" aria-label="Bookmark front">
    <svg class="bookmark__bands" width="300" height="1200" viewBox="0 0 300 1200" aria-hidden="true">
      <polygon points="0,400 300,340 300,915 0,980" fill="var(--blue)"/>
      <polygon points="0,392 220,343 220,354 0,404" fill="var(--green)"/>
      <polygon points="80,965 300,914 300,926 80,977" fill="var(--green)"/>
    </svg>

    <div class="clinic-brand">
      <div class="clinic-brand__mark"></div>
      <div class="clinic-brand__name">BRIGHTWATER</div>
      <div class="clinic-brand__sub">CLINIC</div>
    </div>

    <blockquote class="quote">
      <div class="quote__mark quote__mark--open">&ldquo;</div>
      <div class="quote__frame"></div>
      <p class="quote__text"><b>THE</b><br><span>FIRST</span><br><b>WEALTH</b><br><b>IS</b><br><span>HEALTH</span></p>
      <cite class="quote__author">TOBIAS QUILL HARROW</cite>
      <div class="quote__mark quote__mark--close">&rdquo;</div>
    </blockquote>

    <div class="dental-brand" style="top:1030px">
      <span class="dental-brand__line">HARBOUR DENTAL</span>
      <span class="dental-brand__line dental-brand__line--small">BRIGHTWATER</span>
    </div>
  </section>

  <!-- Back -->
  <section class="bookmark bookmark--back" aria-label="Bookmark back">
    <svg class="bookmark__bands" width="300" height="1200" viewBox="0 0 300 1200" aria-hidden="true">
      <polygon points="0,540 300,475 300,770 0,835" fill="var(--blue)"/>
      <polygon points="0,532 228,481 228,492 0,544" fill="var(--green)"/>
      <polygon points="72,820 300,768 300,780 72,832" fill="var(--green)"/>
    </svg>

    <div class="clinic-brand">
      <div class="clinic-brand__mark"></div>
      <div class="clinic-brand__name">BRIGHTWATER</div>
      <div class="clinic-brand__sub">CLINIC</div>
    </div>

    <div class="icon-row" style="top:318px">
      <span class="icon-badge icon-badge--phone">
        <svg width="18" height="18" viewBox="0 0 24 24" aria-hidden="true"><path fill="var(--green)" d="M6.6 10.8a15.1 15.1 0 0 0 6.6 6.6l2.2-2.2c.3-.3.7-.4 1-.2 1.1.4 2.3.6 3.6.6.6 0 1 .4 1 1V20c0 .6-.4 1-1 1A17 17 0 0 1 3 4c0-.6.4-1 1-1h3.5c.6 0 1 .4 1 1 0 1.3.2 2.5.6 3.6.1.3 0 .7-.2 1z"/></svg>
      </span>
    </div>
    <div class="phone-box" style="top:378px">03 9000 1234</div>

    <div class="icon-row icon-row--light" style="top:567px">
      <span class="icon-badge icon-badge--pin">
        <svg width="20" height="22" viewBox="0 0 24 26" aria-hidden="true"><path fill="none" stroke="var(--blue)" stroke-width="2.4" d="M12 2a7 7 0 0 0-7 7c0 5 7 12 7 12s7-7 7-12a7 7 0 0 0-7-7z"/><circle cx="12" cy="9" r="2.4" fill="var(--blue)"/><path d="M6 24h12" stroke="var(--blue)" stroke-width="2"/></svg>
      </span>
    </div>
    <address class="address">12B<br>Linden Street<br>Brightwater,<br>VIC 3999</address>
    <div class="address-rule"></div>

    <div class="dental-brand" style="top:892px">
      <span class="dental-brand__line">HARBOUR DENTAL</span>
      <span class="dental-brand__line dental-brand__line--small">BRIGHTWATER</span>
    </div>

    <div class="icon-row" style="top:1027px">
      <span class="icon-badge icon-badge--phone">
        <svg width="18" height="18" viewBox="0 0 24 24" aria-hidden="true"><path fill="var(--green)" d="M6.6 10.8a15.1 15.1 0 0 0 6.6 6.6l2.2-2.2c.3-.3.7-.4 1-.2 1.1.4 2.3.6 3.6.6.6 0 1 .4 1 1V20c0 .6-.4 1-1 1A17 17 0 0 1 3 4c0-.6.4-1 1-1h3.5c.6 0 1 .4 1 1 0 1.3.2 2.5.6 3.6.1.3 0 .7-.2 1z"/></svg>
      </span>
    </div>
    <div class="phone-box" style="top:1088px">03 9000 5678</div>
  </section>

</main>
</body>
</html>
```